Card back (63 x 88 mm) design for new "Ember Thornfall" Collectible Trading Card Game

We are looking for something that has a beautiful, stunning, fantasy world feel, but dont forget that this is a card back side. Fonts similar to MagicMedieval and Quill of Ebonreach ("Ember Thornfall" Collectible Trading Card Game). This font will be used later in the front design also. It should be professional, beautiful, refreshing and stunning to look at.
Please feel free to use your imagination, maybe even using fantasy world elements. Feel free to google, "ZeK card back images". We like the style of the black border like you see in the searched images.
We need this in 3 versions. Sizes: like in uploaded pdf will used in the digital version, for the printing house with an additional 5mm extra oversized (every side) and smaller as a picture for a QL Profile Picture.
We want something that is beautiful and inspiring and we can't wait to see what you work on!
Reason: We hope to get more designs
Target Market(s)
Worldwide
Font styles to use
Other font styles liked:
- MagicMedieval, Quill of Ebonreach
Requirements
Must have
- Design must look professional and well integrated.

```html
<!DOCTYPE html>
<html lang="en">
<head>
<meta charset="utf-8">
<title>Ember Thornfall – Card Back</title>
<link href="https://fonts.googleapis.com/css2?family=Uncial+Antiqua&family=Almendra:wght@700&display=swap" rel="stylesheet">
<style>
  :root {
    --page-bg: #ffffff;
    --card-black: #0b0908;
    --card-charcoal: #1a1614;
    --ember-red: #8a1a0c;
    --ember-glow: #c2401c;
    --title-silver: #d9d3cf;
    --subtitle-peach: #f6d2a6;
  }
  * { margin: 0; padding: 0; box-sizing: border-box; }
  html, body {
    width: 1200px;
    height: 900px;
    overflow: hidden;
    background: var(--page-bg);
  }
  .stage {
    position: relative;
    width: 1200px;
    height: 900px;
  }
  .card-back {
    position: absolute;
    left: 326px;
    top: 67px;
    width: 548px;
    height: 766px;
    border-radius: 40px;
    overflow: hidden;
    background:
      repeating-linear-gradient(180deg, rgba(255,255,255,0.012) 0 1px, transparent 1px 3px),
      radial-gradient(ellipse at 50% 50%, var(--card-charcoal) 0%, var(--card-black) 75%);
  }
  .ember-edge {
    position: absolute;
    left: 0;
    width: 100%;
  }
  .ember-edge--top {
    top: 0;
    height: 150px;
    background:
      radial-gradient(ellipse 40% 60% at 0% 30%, rgba(138,26,12,0.55), transparent 70%),
      radial-gradient(ellipse 45% 40% at 100% 20%, rgba(138,26,12,0.5), transparent 70%),
      linear-gradient(180deg, rgba(194,64,28,0.28) 0%, rgba(138,26,12,0.12) 25%, transparent 60%);
  }
  .ember-edge--bottom {
    bottom: 0;
    height: 190px;
    background:
      radial-gradient(ellipse 35% 35% at 80% 55%, rgba(138,26,12,0.5), transparent 70%),
      radial-gradient(ellipse 30% 50% at 100% 40%, rgba(138,26,12,0.45), transparent 70%),
      linear-gradient(0deg, rgba(194,64,28,0.3) 0%, rgba(138,26,12,0.12) 18%, transparent 45%);
  }
  .brand {
    position: absolute;
    left: 0;
    top: 215px;
    width: 100%;
    text-align: center;
  }
  .brand-name {
    font-family: "Uncial Antiqua", serif;
    font-weight: 400;
    color: var(--title-silver);
    line-height: 1.05;
  }
  .brand-name__first { display: block; font-size: 76px; }
  .brand-name__second { display: block; font-size: 66px; }
  .brand-tagline {
    margin-top: 14px;
    font-family: "Almendra", serif;
    font-weight: 700;
    font-size: 20px;
    color: var(--subtitle-peach);
    letter-spacing: 0.3px;
  }
</style>
</head>
<body>
  <main class="stage">
    <section class="card-back">
      <div class="ember-edge ember-edge--top" role="img" aria-label="Glowing ember-burnt torn edge along the top of the card"></div>
      <div class="ember-edge ember-edge--bottom" role="img" aria-label="Glowing ember-burnt torn edge along the bottom of the card"></div>
      <div class="brand">
        <h1 class="brand-name">
          <span class="brand-name__first">Ember</span>
          <span class="brand-name__second">Thornfall</span>
        </h1>
        <p class="brand-tagline">Collectible Trading Card Game</p>
      </div>
    </section>
  </main>
</body>
</html>
```